Quarry Steelworks Capability Statement

Email template to promote our companies capabilities

Target Market(s)

Building companies
Architects

Requirements
Must have
• product list
• Our Products Include
• Boxes
• Brackets
• Boardwalk Frames
• Cable Ladder & Tray
• Cabinets
• Custom Pressings
• Decorative Cladding
• Decorative Panels
• Flashings
• Gates
• Louvered Panels
• Metal Roof Battens
• Metal Scaffold Planks
• Metal Art
• Purlins
• Perforated Metals
• Room Dividers
• Scaffold Planks
• Steel Angles
• Street Furniture
• Shelving & Storage Systems
• Stair Treads
• Stud Framing
• Tanks
• Tool Boxes
• Waste Bins
• Services
• Guillotining
• CNC Bending
• Punching
• Stamping
• Notching
• Cropping
• Coil Blanking
• Turret Punching
• Drilling and tapping
• Welding (MIG & TIG)

```html
<!DOCTYPE html>
<html lang="en">
<head>
<meta charset="utf-8">
<title>Quarry Steelworks – Capability Statement</title>
<link href="https://fonts.googleapis.com/css2?family=Open+Sans:wght@400;600;700&display=swap" rel="stylesheet">
<style>
:root{
  --red:#c8261f;
  --red-dark:#7c2024;
  --ink:#111;
  --grey-bg:#efefef;
  --dark:#262626;
  --muted:#b5b5b5;
  --link:#2a6fff;
}
*{margin:0;padding:0;box-sizing:border-box}
html,body{width:1200px;height:4262px;overflow:hidden;background:#fff}
body{font-family:'Open Sans',Arial,sans-serif;color:var(--ink);position:relative}
.abs{position:absolute}
.header{top:0;left:0;width:1200px;height:280px;background:#fff}
.brand{left:0;width:1200px;top:104px;display:flex;justify-content:center;align-items:center;gap:24px}
.brand-dot{width:64px;height:64px;border-radius:50%;background:var(--red)}
.brand-name{font-size:66px;font-weight:600;color:#7a7a7a;letter-spacing:-1px;line-height:1}
.intro{top:280px;left:0;width:1200px;height:856px;background:linear-gradient(180deg,var(--red) 0%,var(--red-dark) 100%);color:#fff}
.intro h1{position:absolute;top:92px;left:0;width:1200px;text-align:center;font-size:40px;line-height:56px;font-weight:700}
.intro h1 span{font-weight:400}
.intro p{position:absolute;left:100px;width:1000px;font-size:25px;line-height:48px}
.badge{left:918px;top:1056px;width:200px;height:200px;border-radius:50%;background:#fff;box-shadow:0 4px 14px rgba(0,0,0,.25);display:flex;align-items:center;justify-content:center}
.badge div{width:150px;height:150px;border-radius:50%;background:#1d3f95;border:6px solid #fff;outline:4px solid #1d3f95}
.section-title{left:0;width:1200px;text-align:center;font-size:50px;line-height:68px;font-weight:700;letter-spacing:3px;color:var(--red)}
.ticks{list-style:none}
.ticks li{height:54px;display:flex;align-items:center;font-size:23px;font-weight:700;letter-spacing:1.5px;text-transform:uppercase;white-space:nowrap}
.ticks svg{width:28px;height:28px;margin-right:22px;flex:none}
.photo{position:absolute}
.services{top:2892px;left:0;width:1200px;height:802px;background:var(--grey-bg)}
.contacts{top:3694px;left:0;width:1200px;height:568px;background:var(--dark)}
.contacts h2{position:absolute;top:80px;width:1200px;text-align:center;color:#fff;font-size:52px;line-height:70px;font-weight:700;letter-spacing:1px}
.contact-col{position:absolute;font-size:24px;line-height:48px;color:var(--muted)}
.contact-col a{color:var(--link);text-decoration:none}
.pin{left:100px;top:210px;width:44px;height:44px;border-radius:50%;background:#fff;display:flex;align-items:center;justify-content:center}
</style>
</head>
<body>

<header class="abs header">
  <div class="abs brand"><div class="brand-dot"></div><div class="brand-name">QUARRY STEELWORKS</div></div>
</header>

<section class="abs intro">
  <h1>Quarry Steelworks.... <span>Steel Built Right!</span></h1>
  <p style="top:196px">Established in 1981, we manufacture quality steel components to the building, mining and electrical industries. Offering friendly and personalised service for all your steel needs, we can customise our products dependant on our customer needs.</p>
  <p style="top:388px">We have manufacturing locations in Perth, Sydney, Brisbane and Townsville.<br>We pride ourselves on fast turn around to meet our customer’s time frames and flexibility whilst maintaining our excellent value for money and producing high quality products.</p>
  <p style="top:628px">Our experienced fabricators use only the latest in CNC equipment to produce only the highest of quality products and services from larger steel jobs right through to simple spot welding.</p>
</section>

<div class="abs badge" aria-hidden="true"><div></div></div>

<h2 class="abs section-title" style="top:1302px">OUR PRODUCTS</h2>

<svg width="0" height="0" style="position:absolute">
  <symbol id="tick" viewBox="0 0 28 28"><path d="M3 15 L11 23 L25 6" fill="none" stroke="#c8261f" stroke-width="5" stroke-linecap="round" stroke-linejoin="round"/></symbol>
</svg>

<ul class="abs ticks" style="left:100px;top:1397px">
  <li><svg><use href="#tick"/></svg>Boxes</li>
  <li><svg><use href="#tick"/></svg>Brackets</li>
  <li><svg><use href="#tick"/></svg>Boardwalk Frames</li>
  <li><svg><use href="#tick"/></svg>Cable Ladder &amp; Tray</li>
  <li><svg><use href="#tick"/></svg>Cabinets</li>
  <li><svg><use href="#tick"/></svg>Custom Pressings</li>
  <li><svg><use href="#tick"/></svg>Decorative Cladding</li>
  <li><svg><use href="#tick"/></svg>Decorative Panels</li>
  <li><svg><use href="#tick"/></svg>Flashings</li>
  <li><svg><use href="#tick"/></svg>Gates</li>
  <li><svg><use href="#tick"/></svg>Louvered Panels</li>
  <li><svg><use href="#tick"/></svg>Metal Roof Battens</li>
  <li><svg><use href="#tick"/></svg>Metal Scaffold Planks</li>
  <li><svg><use href="#tick"/></svg>Metal Art</li>
  <li><svg><use href="#tick"/></svg>Purlins</li>
  <li><svg><use href="#tick"/></svg>Perforated Metals</li>
  <li><svg><use href="#tick"/></svg>Room Dividers</li>
  <li><svg><use href="#tick"/></svg>Scaffold Planks</li>
  <li><svg><use href="#tick"/></svg>Steel Angles</li>
  <li><svg><use href="#tick"/></svg>Street Furniture</li>
  <li><svg><use href="#tick"/></svg>Shelving &amp; Storage Systems</li>
  <li><svg><use href="#tick"/></svg>Stair Treads</li>
  <li><svg><use href="#tick"/></svg>Stud Framing</li>
  <li><svg><use href="#tick"/></svg>Tanks</li>
  <li><svg><use href="#tick"/></svg>Tool Boxes</li>
  <li><svg><use href="#tick"/></svg>Waste Bins</li>
</ul>

<div class="photo" role="img" aria-label="Steel roof trusses and wall framing on a house build" style="left:600px;top:1416px;width:600px;height:226px;background:linear-gradient(180deg,#b9c7d6,#8c8f92 60%,#7a5d4c)"></div>
<div class="photo" role="img" aria-label="Stacked galvanised steel angles" style="left:600px;top:1646px;width:298px;height:226px;background:linear-gradient(135deg,#5f6366,#d4d7da 50%,#6b6f72)"></div>
<div class="photo" role="img" aria-label="Bundled steel purlin sections" style="left:902px;top:1646px;width:298px;height:226px;background:linear-gradient(135deg,#3f4a55,#b8c2cb 60%,#7f8a94)"></div>
<div class="photo" role="img" aria-label="Colourful perforated metal seating" style="left:600px;top:1876px;width:298px;height:226px;background:linear-gradient(120deg,#2d6fb4,#c7472b 50%,#98a0a6)"></div>
<div class="photo" role="img" aria-label="Steel bike rack on grass" style="left:902px;top:1876px;width:124px;height:226px;background:linear-gradient(180deg,#8f9a9e,#4f6b2e)"></div>
<div class="photo" role="img" aria-label="Perforated steel street waste bin" style="left:1030px;top:1876px;width:170px;height:226px;background:linear-gradient(180deg,#c9c5bd,#6e6458)"></div>
<div class="photo" role="img" aria-label="Building facade clad in perforated panels" style="left:600px;top:2106px;width:298px;height:226px;background:linear-gradient(135deg,#9a6a4c,#d9dcdf 55%,#8e9297)"></div>
<div class="photo" role="img" aria-label="Shopfront with decorative laser-cut screens" style="left:902px;top:2106px;width:298px;height:226px;background:linear-gradient(180deg,#9c1e1b,#6d2a22 40%,#5b5e61)"></div>
<div class="photo" role="img" aria-label="Garden wall with decorative metal panels" style="left:600px;top:2336px;width:600px;height:226px;background:linear-gradient(180deg,#c3cfd8,#d7d4ca 50%,#5e7a35)"></div>
<div class="photo" role="img" aria-label="Modern house with decorative screen balcony" style="left:600px;top:2566px;width:298px;height:226px;background:linear-gradient(180deg,#6d9fd6,#dcdcdc 45%,#5a4a40)"></div>
<div class="photo" role="img" aria-label="House with metal balustrade and garage door" style="left:902px;top:2566px;width:298px;height:226px;background:linear-gradient(180deg,#cfd4d8,#f0f0f0 60%,#9a9a96)"></div>

<section class="abs services">
  <h2 class="abs section-title" style="top:82px">OUR SERVICES</h2>
  <div class="photo" role="img" aria-label="CNC press brake in the factory" style="left:0;top:198px;width:600px;height:226px;background:linear-gradient(180deg,#5b6670,#c8372c 55%,#6e6a60)"></div>
  <div class="photo" role="img" aria-label="Fabricator working in the workshop" style="left:0;top:428px;width:298px;height:226px;background:linear-gradient(180deg,#516a7d,#8c8778 60%,#d0a52b)"></div>
  <div class="photo" role="img" aria-label="Stacked steel framing in the warehouse" style="left:302px;top:428px;width:298px;height:226px;background:linear-gradient(135deg,#6b7075,#d5d8db 50%,#595d61)"></div>
  <ul class="abs ticks" style="left:686px;top:179px">
    <li><svg><use href="#tick"/></svg>Guillotining</li>
    <li><svg><use href="#tick"/></svg>CNC Bending</li>
    <li><svg><use href="#tick"/></svg>Punching</li>
    <li><svg><use href="#tick"/></svg>Stamping</li>
    <li><svg><use href="#tick"/></svg>Notching</li>
    <li><svg><use href="#tick"/></svg>Cropping</li>
    <li><svg><use href="#tick"/></svg>Coil Blanking</li>
    <li><svg><use href="#tick"/></svg>Turret Punching</li>
    <li><svg><use href="#tick"/></svg>Drilling and Tapping</li>
    <li><svg><use href="#tick"/></svg>Welding (MIG &amp; TIG)</li>
  </ul>
</section>

<footer class="abs contacts">
  <h2>CONTACTS</h2>
  <div class="abs pin" aria-hidden="true">
    <svg width="24" height="24" viewBox="0 0 24 24"><path d="M21 3 L3 11 L11 13 L13 21 Z" fill="#c8261f"/></svg>
  </div>
  <div class="contact-col" style="left:180px;top:194px">
    Head Office<br>08 9400 2211<br>Dan Keller<br>State Manager<br>08 9300 4107<br><a href="mailto:d.keller@quarrysteelworks.com.au">d.keller@quarrysteelworks.com.au</a>
  </div>
  <div class="contact-col" style="left:658px;top:242px">
    Mark Elston<br>Sales Manager<br>08 9300 4152<br><a href="mailto:mark.elston@quarrysteelworks.com.au">mark.elston@quarrysteelworks.com.au</a>
  </div>
</footer>

</body>
</html>
```